Market online tutoring + Back to School + give Support for students school work K to 12 Grade

To promote my tutoring business online need to create a two sided flyer. Need to get the attention of parents and educators who looking for help to support the digital learning of their students due to COVID-19 lock down. I need to project and differentiate that we offer support for online school with individualized learning . We tutor Elementary to High school students on all subjects you may take a look at my website qnacademyga.com for additional info and also I can provide
Updates

Hi All Due to Covid, we were unable to work on this project on time as originally planned. We were given an extension until March 15 and we will complete it by then. Sorry for any inconvenience and Thank you for your support. -QN Academy

Target Market(s)

Parents and students

Industry/Entity Type

Education

Requirements
Must have
• For online less fine print on the first page. The phone number and support text message. Back to School , Support Online learning KEV/NUR test prep should have some focus
Nice to have
• Discuss the platform We created a platform with live instructor interaction, virtual classroom, instructional videos, assessments, and practice to support every individual student’s need. We are confident in our ability to provide the most effective distance learning experience.
Should not have
• too much clunky and packed with content. Should be easy to read with color

```html
<!DOCTYPE html>
<html lang="en">
<head>
<meta charset="utf-8">
<title>QN Academy – Two-Sided Flyer</title>
<link href="https://fonts.googleapis.com/css2?family=Montserrat:ital,wght@0,400;0,500;0,600;0,700;0,800;1,400;1,500&family=Open+Sans:wght@400;600;700&family=Oswald:wght@600;700&family=Patrick+Hand&display=swap" rel="stylesheet">
<style>
  :root{
    --red:#d2232f;
    --red-deep:#b31d2a;
    --teal:#0d3a4b;
    --teal-dark:#0a2e3c;
    --beige:#ecd4b6;
    --beige-light:#f2e0c9;
    --white:#ffffff;
    --ink:#1d2a33;
    --muted:#555d63;
    --bg:#e9e9ea;
  }
  *{box-sizing:border-box;margin:0;padding:0}
  html,body{width:1200px;height:906px;overflow:hidden;background:var(--bg)}
  body{position:relative;font-family:"Montserrat",sans-serif}
  .page{position:absolute;top:104px;width:492px;height:697px;overflow:hidden;background:var(--teal)}
  .page--front{left:76px;background:var(--beige)}
  .page--back{left:630px}
  .page__bg{position:absolute;inset:0}
  .abs{position:absolute}

  /* front */
  .front-photo{left:170px;top:40px;width:322px;height:270px;background:radial-gradient(ellipse at 60% 50%,#e2c29d 0%,#ecd4b6 70%,rgba(236,212,182,0) 100%)}
  .exam-line{left:28px;top:20px;font-family:"Montserrat",sans-serif;font-weight:700;font-size:29px;color:var(--teal);letter-spacing:-.5px}
  .headline{left:28px;top:58px;line-height:1}
  .headline .big{display:block;font-weight:800;font-size:40px;color:var(--red-deep);letter-spacing:1px}
  .headline .small{display:block;font-style:italic;font-weight:500;font-size:27px;color:var(--teal);margin:2px 0 8px 4px}
  .brand-mark{left:354px;top:236px;width:126px;height:126px;border-radius:50%;background:var(--teal);border:4px solid var(--beige-light);display:flex;align-items:center;justify-content:center;text-align:center}
  .brand-mark span{font-weight:700;font-size:17px;color:var(--beige-light);line-height:1.1}
  .platform-title{left:22px;top:298px;font-weight:700;font-size:15px;color:var(--white)}
  .feature{display:flex;align-items:center;gap:10px;color:var(--white);font-size:14.5px;line-height:1.1}
  .feature svg{flex:none}
  .confidence{left:34px;top:474px;width:420px;color:var(--white);font-size:14.5px;line-height:1.4}
  .cta-box{left:23px;top:531px;width:449px;height:92px;background:var(--white);border-radius:4px;text-align:center;padding-top:6px}
  .cta-box .cta-main{font-family:"Oswald",sans-serif;font-weight:700;font-size:30px;color:var(--red-deep);letter-spacing:.5px;line-height:1.05}
  .cta-box .cta-sub{font-family:"Patrick Hand",cursive;font-size:26px;color:var(--teal);line-height:1}
  .cta-box .cta-note{font-style:italic;font-size:12px;color:#4a4f53;margin-top:2px}
  .front-contact{top:636px;color:var(--white);text-align:center;line-height:1.05}
  .front-contact .label{font-size:20px}
  .front-contact .value{font-weight:700;font-size:23px}

  /* back */
  .back-photo{left:0;top:0;width:492px;height:215px;background:linear-gradient(180deg,#efe9e3 0%,#d9cfc3 60%,#c9b9a8 100%)}
  .section-title{left:24px;color:var(--white);font-weight:700;font-size:17px}
  .rule{left:24px;width:434px;height:1px;background:rgba(255,255,255,.55)}
  .why-item{width:150px;color:var(--white)}
  .why-item h3{font-weight:700;font-size:9.5px;margin:0 0 4px 36px}
  .why-item p{font-family:"Open Sans",sans-serif;font-size:7.6px;line-height:1.45;text-align:justify;margin-left:36px;width:98px}
  .why-item svg{position:absolute;left:0;top:-2px}
  .plan{top:450px;width:127px;height:138px;background:#f2f2f2;border-radius:3px;text-align:center}
  .plan__head{height:32px;background:var(--red);color:var(--white);font-weight:700;font-size:10.5px;line-height:32px;border-radius:3px 3px 0 0}
  .plan__body{font-family:"Open Sans",sans-serif;font-size:8px;color:#555;line-height:15px;padding-top:10px}
  .plan__body .rate{color:var(--red);font-weight:700}
  .plan__price{position:absolute;left:27px;top:122px;width:62px;height:27px;background:var(--red);color:var(--white);font-weight:700;font-size:17px;line-height:25px;border-radius:7px;border:2px solid var(--white)}
  .back-button{top:613px;height:62px;background:var(--white);border-radius:4px;text-align:center;color:var(--red);line-height:1.05;padding-top:7px}
  .back-button .label{font-size:20px}
  .back-button .value{font-weight:700;font-size:22px}
</style>
</head>
<body>

<!-- FRONT -->
<section class="page page--front" aria-label="Flyer front">
  <div class="abs front-photo" role="img" aria-label="Photo of two smiling children with school backpacks lying on the floor as if flying"></div>

  <svg class="page__bg" width="492" height="697" viewBox="0 0 492 697">
    <path d="M0,215 Q250,282 492,288 L492,697 L0,697 Z" fill="var(--teal)"/>
    <path d="M0,235 Q250,300 492,302 L492,697 L0,697 Z" fill="var(--red)"/>
    <path d="M0,580 L0,697 L492,697 L492,560 Q380,640 0,580 Z" fill="var(--teal)"/>
  </svg>

  <div class="abs exam-line">KEV NUR</div>
  <div class="abs headline">
    <span class="big">LEARN</span>
    <span class="small">Any Where</span>
    <span class="big">LEARN</span>
    <span class="small">Online</span>
  </div>

  <div class="abs brand-mark"><span>QN<br>Academy</span></div>

  <div class="abs platform-title">We created a platform with</div>

  <div class="abs feature" style="left:32px;top:329px">
    <svg width="36" height="28" viewBox="0 0 36 28"><rect x="4" y="2" width="28" height="19" rx="2" fill="#fff"/><circle cx="18" cy="9" r="3.5" fill="var(--red)"/><path d="M12,18 Q18,11 24,18 Z" fill="var(--red)"/><rect x="0" y="22" width="36" height="4" rx="1" fill="#fff"/></svg>
    <span>Live instructor<br>Interaction</span>
  </div>
  <div class="abs feature" style="left:32px;top:379px">
    <svg width="36" height="28" viewBox="0 0 36 28"><path d="M2,3 L17,6 L17,26 L2,23 Z M19,6 L34,3 L34,23 L19,26 Z" fill="#fff"/><path d="M23,10 L30,14 L23,18 Z" fill="var(--red)"/></svg>
    <span>Virtual<br>Classroom</span>
  </div>
  <div class="abs feature" style="left:32px;top:423px">
    <svg width="36" height="32" viewBox="0 0 36 32"><rect x="3" y="1" width="22" height="27" rx="2" fill="#fff"/><path d="M7,8h4M7,14h4M7,20h4M13,8h8M13,14h8M13,20h6" stroke="var(--red)" stroke-width="2"/><circle cx="27" cy="24" r="8" fill="#fff"/><path d="M25,20 L31,24 L25,28 Z" fill="var(--red)"/></svg>
    <span>Instructional<br>Videos</span>
  </div>
  <div class="abs feature" style="left:210px;top:331px">
    <svg width="32" height="32" viewBox="0 0 34 32"><rect x="2" y="3" width="26" height="27" rx="2" fill="#fff"/><path d="M6,10h4M6,17h4M6,24h4M13,10h11M13,17h11M13,24h11" stroke="var(--red)" stroke-width="2"/><rect x="27" y="6" width="5" height="22" fill="#fff"/></svg>
    <span>Assessments<br>&amp; Practice</span>
  </div>
  <div class="abs feature" style="left:210px;top:384px">
    <svg width="32" height="40" viewBox="0 0 34 40"><path d="M5,8 L17,3 L29,8 L17,13 Z" fill="#fff"/><circle cx="17" cy="17" r="7" fill="#fff"/><path d="M3,40 Q3,26 17,26 Q31,26 31,40 Z" fill="#fff"/></svg>
    <span>Support every<br>Individual Student’s need.</span>
  </div>

  <p class="abs confidence">We are confident in our ability to provide&nbsp; the most effective distance learning experience.</p>

  <div class="abs cta-box">
    <div class="cta-main">CONTINUE LEARNING FROM HOME</div>
    <div class="cta-sub">Digital learning during COVID-19 lockdown.</div>
    <div class="cta-note">We tutor Elementary to High school students on all subjects</div>
  </div>

  <div class="abs front-contact" style="left:48px;width:170px">
    <div class="label">Call us</div>
    <div class="value">555-014-2287</div>
  </div>
  <div class="abs front-contact" style="left:260px;width:210px;top:639px">
    <div class="label">Visit us</div>
    <div class="value" style="font-size:20px">qnacademyga.com</div>
  </div>
</section>

<!-- BACK -->
<section class="page page--back" aria-label="Flyer back">
  <div class="abs back-photo" role="img" aria-label="Photo of two young children using laptops in a bright playroom"></div>
  <svg class="page__bg" width="492" height="697" viewBox="0 0 492 697">
    <path d="M0,165 Q260,150 492,205 L492,214 Q260,168 0,180 Z" fill="var(--red)"/>
    <path d="M0,180 Q260,168 492,214 L492,697 L0,697 Z" fill="var(--teal)"/>
    <path d="M0,645 Q246,610 492,640 L492,697 L0,697 Z" fill="var(--red)"/>
  </svg>

  <h2 class="abs section-title" style="top:188px">Why us</h2>
  <div class="abs rule" style="top:212px"></div>

  <div class="abs why-item" style="left:24px;top:224px">
    <svg width="28" height="26" viewBox="0 0 28 26"><path d="M4,16 V12 A10,10 0 0 1 24,12 V16" stroke="#fff" stroke-width="2.4" fill="none"/><rect x="2" y="14" width="6" height="10" rx="2" fill="#fff"/><rect x="20" y="14" width="6" height="10" rx="2" fill="#fff"/></svg>
    <h3>Support</h3>
    <p>Lorem ipsum dolor sit amet, consectetur adipi-scing elit, sed do eiusmod tempor incididunt ut labore et dolore magna aliqua.</p>
  </div>
  <div class="abs why-item" style="left:166px;top:224px">
    <svg width="28" height="26" viewBox="0 0 28 26"><rect x="4" y="1" width="16" height="21" rx="2" fill="#fff"/><circle cx="12" cy="9" r="3" fill="var(--teal)"/><circle cx="21" cy="19" r="6" fill="#fff" stroke="var(--teal)" stroke-width="1.5"/><path d="M18,19 l2,2 l4,-4" stroke="var(--teal)" stroke-width="1.6" fill="none"/></svg>
    <h3>Effective Curriculum</h3>
    <p>Lorem ipsum dolor sit amet, consectetur adipi-scing elit, sed do eiusmod tempor incididunt ut labore et dolore magna aliqua.</p>
  </div>
  <div class="abs why-item" style="left:314px;top:224px">
    <svg width="28" height="26" viewBox="0 0 28 26"><rect x="11" y="2" width="15" height="11" fill="none" stroke="#fff" stroke-width="2"/><circle cx="6" cy="5" r="3" fill="#fff"/><path d="M3,10 h6 v6 h-1 v8 h-4 v-8 h-1 Z" fill="#fff"/><path d="M9,12 L14,8" stroke="#fff" stroke-width="1.6"/></svg>
    <h3>Awesome Teachers</h3>
    <p>Lorem ipsum dolor sit amet, consectetur adipi-scing elit, sed do eiusmod tempor incididunt ut labore et dolore magna aliqua.</p>
  </div>
  <div class="abs why-item" style="left:24px;top:320px">
    <svg width="28" height="26" viewBox="0 0 28 26"><path d="M8,12 V7 A6,6 0 0 1 20,7" stroke="#fff" stroke-width="2.4" fill="none"/><rect x="5" y="12" width="14" height="12" rx="1.5" fill="#fff"/><circle cx="12" cy="18" r="1.8" fill="var(--teal)"/></svg>
    <h3>Unlimited access</h3>
    <p>Lorem ipsum dolor sit amet, consectetur adipi-scing elit, sed do eiusmod tempor incididunt ut labore et dolore magna aliqua.</p>
  </div>
  <div class="abs why-item" style="left:166px;top:320px">
    <svg width="28" height="26" viewBox="0 0 28 26"><path d="M3,3 H13 L25,15 L15,25 L3,13 Z" fill="#fff"/><circle cx="8" cy="8" r="2" fill="var(--teal)"/></svg>
    <h3>Easy Pricing</h3>
    <p>Lorem ipsum dolor sit amet, consectetur adipi-scing elit, sed do eiusmod tempor incididunt ut labore et dolore magna aliqua.</p>
  </div>
  <div class="abs why-item" style="left:314px;top:320px">
    <svg width="28" height="26" viewBox="0 0 28 26"><rect x="2" y="1" width="24" height="15" rx="1" fill="#fff"/><path d="M7,4 L13,5 V13 L7,12 Z M15,5 L21,4 V12 L15,13 Z" fill="var(--teal)"/><path d="M6,21 a3,3 0 1 0 8,0 a3,3 0 1 0 8,0 a3,3 0 1 0 -8,0 a3,3 0 1 0 -8,0" stroke="#fff" stroke-width="1.6" fill="none"/></svg>
    <h3 style="width:140px">Unlimited Online practice</h3>
    <p>Lorem ipsum dolor sit amet, consectetur adipi-scing elit, sed do eiusmod tempor incididunt ut labore et dolore magna aliqua.</p>
  </div>

  <h2 class="abs section-title" style="top:412px">Available Courses</h2>
  <div class="abs rule" style="top:438px"></div>

  <div class="abs plan" style="left:26px">
    <div class="plan__head">Starter</div>
    <div class="plan__body"><div class="rate">Monthly Plan&nbsp; $100</div>Unlimited Course Access<br>Unlimited online Practice<br>24x7 support<br>Certification</div>
    <div class="plan__price">$100</div>
  </div>
  <div class="abs plan" style="left:185px">
    <div class="plan__head">Medium</div>
    <div class="plan__body"><div class="rate">Monthly Plan&nbsp; $200</div>Unlimited Course Access<br>Unlimited online Practice<br>24x7 support<br>Certification</div>
    <div class="plan__price">$200</div>
  </div>
  <div class="abs plan" style="left:335px">
    <div class="plan__head">Premium</div>
    <div class="plan__body"><div class="rate">Monthly Plan&nbsp; $300</div>Unlimited Course Access<br>Unlimited online Practice<br>24x7 support<br>Certification</div>
    <div class="plan__price">$300</div>
  </div>

  <div class="abs back-button" style="left:29px;width:195px">
    <div class="label">Call us</div>
    <div class="value">555-014-2287</div>
  </div>
  <div class="abs back-button" style="left:243px;width:219px">
    <div class="label">Visit us</div>
    <div class="value" style="font-size:20px">qnacademyga.com</div>
  </div>
</section>

</body>
</html>
```